Business Cards and email stationery for VoiceOver Artist
Cutting Edge Business cards and email stationery for VoiceOver Artist
Use standard fonts
Not sure here?
Bright & Fun-filled
Marcus Dellow
Voiceover
2817 Palmera Ave
Encino CA 91427
(•••NO ADDRESS ON BUSINESS CARDS PLEASE••••)
818-555-2193 Cell
marcus@marcusdellow.example
marcusdellow.example
As 3-D as possible, cutting-edge, creative
1 Should be easy to read
2 Cell number should be listed first!
Uploaded Logo for VoiceOver Artist for Business cards and email Stationery
Logo for VoiceOver Artist v2

```html
<!DOCTYPE html>
<html lang="en">
<head>
<meta charset="utf-8">
<title>Marcus Dellow Voiceover – Business Cards</title>
<link rel="stylesheet" href="https://fonts.googleapis.com/css2?family=Montserrat:wght@600;700&family=Open+Sans:wght@400;600&family=Cormorant+SC:wght@500&display=swap">
<style>
  :root {
    --page: #ffffff;
    --red-deep: #6e0a0a;
    --red: #c11414;
    --red-bright: #e63a3a;
    --charcoal: #2b2b2b;
    --black: #0d0d0d;
    --paper: #f2f2f2;
    --silver-light: #f4f4f4;
    --silver: #b9b9b9;
    --silver-dark: #6a6a6a;
    --ink-light: #ffffff;
    --label: #c9c9c9;
  }
  * { margin: 0; padding: 0; box-sizing: border-box; }
  html, body { width: 1200px; height: 811px; overflow: hidden; background: var(--page); }
  .sheet { position: relative; width: 1200px; height: 811px; }
  .card {
    position: absolute; width: 547px; height: 312px;
    border-radius: 22px; overflow: hidden;
    box-shadow: 0 2px 5px rgba(0,0,0,.25);
  }
  .card-art { position: absolute; inset: 0; width: 100%; height: 100%; }
  .front-one { left: 24px; top: 19px; }
  .front-two { left: 629px; top: 19px; }
  .back-one  { left: 24px; top: 425px; }
  .back-two  { left: 629px; top: 425px; }

  .label {
    position: absolute; width: 547px; text-align: center;
    font-family: "Cormorant SC", serif; font-size: 22px; color: var(--label);
    letter-spacing: 1px;
  }
  .label-front-one { left: 24px; top: 346px; }
  .label-front-two { left: 629px; top: 346px; }
  .label-back-one  { left: 24px; top: 760px; }
  .label-back-two  { left: 629px; top: 760px; }

  .identity { position: absolute; color: var(--ink-light); }
  .identity .name {
    font-family: "Montserrat", sans-serif; font-weight: 700;
    font-size: 25px; letter-spacing: 0.5px; text-transform: uppercase; line-height: 1;
    white-space: nowrap;
  }
  .identity .role {
    font-family: "Montserrat", sans-serif; font-weight: 600;
    font-size: 9px; letter-spacing: 9px; text-transform: uppercase;
    margin-top: 6px; opacity: .8;
  }
  .identity.right { text-align: right; }

  .contacts {
    position: absolute; list-style: none;
    font-family: "Open Sans", sans-serif; font-size: 14px; color: var(--ink-light);
    line-height: 22px;
  }
  .contacts li { display: flex; align-items: center; gap: 7px; }
  .contacts.right li { justify-content: flex-end; }
  .contacts svg { width: 12px; height: 12px; flex: none; }

  .web {
    position: absolute; bottom: 16px;
    font-family: "Open Sans", sans-serif; font-size: 14px; letter-spacing: 5px;
  }
</style>
</head>
<body>
<main class="sheet">
  <svg width="0" height="0" style="position:absolute">
    <defs>
      <linearGradient id="red-sheen" x1="0" y1="0" x2="0" y2="1">
        <stop offset="0" stop-color="#8a0f0f"/>
        <stop offset=".45" stop-color="#e02b2b"/>
        <stop offset=".55" stop-color="#c11414"/>
        <stop offset="1" stop-color="#5e0808"/>
      </linearGradient>
      <radialGradient id="red-glow" cx=".35" cy=".45" r=".8">
        <stop offset="0" stop-color="#ef4141"/>
        <stop offset=".6" stop-color="#b31212"/>
        <stop offset="1" stop-color="#4d0606"/>
      </radialGradient>
      <linearGradient id="dark-sheen" x1="0" y1="0" x2="0" y2="1">
        <stop offset="0" stop-color="#3a3a3a"/>
        <stop offset="1" stop-color="#1f1f1f"/>
      </linearGradient>
      <linearGradient id="silver" x1="0" y1="0" x2="1" y2="1">
        <stop offset="0" stop-color="#fafafa"/>
        <stop offset=".5" stop-color="#c4c4c4"/>
        <stop offset="1" stop-color="#6d6d6d"/>
      </linearGradient>
    </defs>
  </svg>

  <!-- Front 1 -->
  <section class="card front-one">
    <svg class="card-art" viewBox="0 0 547 312">
      <rect width="547" height="312" fill="var(--paper)"/>
      <path d="M196 0 Q300 156 196 312 L547 312 L547 0 Z" fill="url(#red-sheen)"/>
      <path d="M184 0 Q288 156 184 312" fill="none" stroke="var(--silver)" stroke-width="4"/>
      <circle cx="118" cy="154" r="104" fill="url(#silver)"/>
    </svg>
    <div class="identity right" style="right:28px; top:118px;">
      <div class="name">Marcus Dellow</div>
      <div class="role">Voiceover</div>
    </div>
    <ul class="contacts right" style="right:28px; top:186px;">
      <li>818-555-2193 <svg viewBox="0 0 12 12"><circle cx="6" cy="6" r="6" fill="#fff"/></svg></li>
      <li>marcus@marcusdellow.example <svg viewBox="0 0 12 12"><circle cx="6" cy="6" r="6" fill="#fff"/></svg></li>
      <li>marcusdellow.example <svg viewBox="0 0 12 12"><circle cx="6" cy="6" r="6" fill="#fff"/></svg></li>
    </ul>
  </section>
  <div class="label label-front-one">Front-1</div>

  <!-- Front 2 -->
  <section class="card front-two">
    <svg class="card-art" viewBox="0 0 547 312">
      <rect width="547" height="312" fill="url(#dark-sheen)"/>
      <path d="M351 0 Q247 156 351 312 L547 312 L547 0 Z" fill="var(--paper)"/>
      <path d="M363 0 Q259 156 363 312" fill="none" stroke="var(--red)" stroke-width="5"/>
      <circle cx="436" cy="150" r="104" fill="url(#silver)"/>
    </svg>
    <div class="identity" style="left:24px; top:118px;">
      <div class="name">Marcus Dellow</div>
      <div class="role">Voiceover</div>
    </div>
    <ul class="contacts" style="left:24px; top:186px;">
      <li><svg viewBox="0 0 12 12"><circle cx="6" cy="6" r="6" fill="#fff"/></svg>818-555-2193 Cell</li>
      <li><svg viewBox="0 0 12 12"><circle cx="6" cy="6" r="6" fill="#fff"/></svg>marcus@marcusdellow.example</li>
      <li><svg viewBox="0 0 12 12"><circle cx="6" cy="6" r="6" fill="#fff"/></svg>marcusdellow.example</li>
    </ul>
  </section>
  <div class="label label-front-two">Front-2</div>

  <!-- Back 1 -->
  <section class="card back-one">
    <svg class="card-art" viewBox="0 0 547 312">
      <rect width="547" height="312" fill="var(--black)"/>
      <circle cx="436" cy="148" r="108" fill="url(#silver)"/>
    </svg>
    <div class="identity" style="left:28px; top:134px;">
      <div class="name">Marcus Dellow</div>
      <div class="role">Voiceover</div>
    </div>
    <div class="web" style="left:28px; color:var(--red);">www.marcusdellow.example</div>
  </section>
  <div class="label label-back-one">Back-1</div>

  <!-- Back 2 -->
  <section class="card back-two">
    <svg class="card-art" viewBox="0 0 547 312">
      <rect width="547" height="312" fill="url(#red-glow)"/>
      <circle cx="124" cy="148" r="108" fill="url(#silver)"/>
    </svg>
    <div class="identity right" style="right:24px; top:134px;">
      <div class="name">Marcus Dellow</div>
      <div class="role">Voiceover</div>
    </div>
    <div class="web" style="right:24px; color:var(--charcoal);">www.marcusdellow.example</div>
  </section>
  <div class="label label-back-two">Back-2</div>
</main>
</body>
</html>
```